Business Card design for construction company

I would like a business card design for a construction company - Harlow Constructions. I have attached the ai logo file for use. I would like the card to be very smart and clean and incorporate only white and the two colours in the logo. I would like the card to have two sides. One side can just have the logo, the other with the relevant information.

Target Market(s)

Building and Construction Clients

Industry/Entity Type

Business

Contact Information for Business Card

Name: Tom Pardoe
Company: Harlow Constructions Pty Limited
Address: 14 Mallee Crescent Carrow Vale 2093
Phone: 0427 531 068
Email: tomp@harlowbuild-example.com.au

Font styles to use
Serif
Sans Serif

Requirements
Must have
• Details noted above
• Logo as provided
• Colours as in logo
• Square edges
• A font that compliments the logo
Should not have
• Any colour other than white and those in logo
• Rounded edges

```html
<!DOCTYPE html>
<html lang="en">
<head>
<meta charset="utf-8">
<title>Harlow Constructions – Stationery</title>
<link href="https://fonts.googleapis.com/css2?family=Roboto:wght@300;400;500&display=swap" rel="stylesheet">
<style>
  :root {
    --bg: #efefef;
    --paper: #ffffff;
    --ink: #58595b;
    --ink-dark: #3d3e40;
    --accent: #1ea0dc;
    --card-dark: #58595b;
  }
  * { box-sizing: border-box; margin: 0; padding: 0; }
  html, body { width: 1200px; height: 1200px; overflow: hidden; }
  body {
    background: var(--bg);
    font-family: "Roboto", Arial, sans-serif;
    color: var(--ink);
    position: relative;
  }
  .wordmark {
    display: flex; align-items: center;
    font-weight: 300; text-transform: uppercase; letter-spacing: 0.14em;
    color: var(--ink); white-space: nowrap;
  }
  .wordmark__dot { background: var(--accent); flex: none; }

  /* Letterhead */
  .letterhead {
    position: absolute; left: 140px; top: 210px; width: 586px; height: 773px;
    background: var(--paper);
  }
  .letterhead .wordmark { position: absolute; left: 49px; top: 60px; font-size: 14px; }
  .letterhead .wordmark__dot { width: 7px; height: 7px; margin-right: 10px; }
  .letterhead__address {
    position: absolute; right: 202px; top: 56px;
    font-size: 9px; line-height: 12px; text-align: right; color: var(--ink-dark);
  }
  .letterhead__divider {
    position: absolute; left: 394px; top: 58px; width: 1px; height: 22px; background: var(--ink-dark);
  }
  .letterhead__contact {
    position: absolute; left: 404px; top: 56px; font-size: 9px; line-height: 12px; color: var(--ink-dark);
  }
  .contact-row { display: flex; align-items: center; gap: 4px; }
  .contact-row svg { flex: none; fill: var(--accent); }
  .letterhead__rule {
    position: absolute; left: 48px; top: 725px; width: 491px; height: 1px; background: var(--ink-dark);
  }
  .letterhead__web {
    position: absolute; right: 45px; top: 731px; font-size: 8.5px; font-weight: 500; color: var(--ink-dark);
  }
  .letterhead__web span { color: var(--accent); }

  /* Business card – details side */
  .card { position: absolute; width: 271px; }
  .card--details { left: 796px; top: 211px; height: 153px; background: var(--paper); }
  .card--details .wordmark { position: absolute; left: 17px; top: 31px; font-size: 7px; }
  .card--details .wordmark__dot { width: 4px; height: 4px; margin-right: 5px; }
  .card__name {
    position: absolute; left: 17px; top: 78px; font-size: 10px; font-weight: 500; color: var(--ink-dark);
  }
  .card__role { position: absolute; left: 17px; top: 91px; font-size: 5.5px; color: var(--accent); }
  .card__rule { position: absolute; left: 17px; top: 102px; width: 236px; height: 1px; background: var(--ink); }
  .card__contact {
    position: absolute; left: 17px; top: 110px; font-size: 5.5px; line-height: 8.5px; font-weight: 500; color: var(--ink-dark);
  }
  .card__contact svg { width: 5px; height: 5px; }
  .card__address {
    position: absolute; right: 18px; top: 118px; font-size: 5.5px; line-height: 8.5px; text-align: right; font-weight: 500; color: var(--ink-dark);
  }

  /* Business card – logo side */
  .card--logo {
    left: 796px; top: 418px; width: 270px; height: 158px; background: var(--card-dark);
    display: flex; align-items: center; justify-content: center; padding-bottom: 34px;
  }
  .card--logo .wordmark { color: var(--paper); font-size: 11px; }
  .card--logo .wordmark__dot { width: 6px; height: 6px; margin-right: 8px; }
</style>
</head>
<body>

<section class="letterhead" aria-label="Letterhead">
  <div class="wordmark"><span class="wordmark__dot"></span>Harlow Constructions</div>
  <address class="letterhead__address" style="font-style:normal">14 Mallee Crescent<br>Carrow Vale 2093</address>
  <div class="letterhead__divider"></div>
  <div class="letterhead__contact">
    <div class="contact-row">
      <svg width="7" height="7" viewBox="0 0 24 24" aria-hidden="true"><path d="M6.6 10.8a15.1 15.1 0 0 0 6.6 6.6l2.2-2.2c.3-.3.7-.4 1-.2 1.1.4 2.3.6 3.6.6.6 0 1 .4 1 1V20c0 .6-.4 1-1 1A17 17 0 0 1 3 4c0-.6.4-1 1-1h3.5c.6 0 1 .4 1 1 0 1.3.2 2.5.6 3.6.1.3 0 .7-.2 1z"/></svg>
      0427 531 068
    </div>
    <div class="contact-row">
      <svg width="7" height="7" viewBox="0 0 24 24" aria-hidden="true"><path d="M2 5h20v14H2zm2 2v.5l8 5 8-5V7l-8 5z"/></svg>
      tomp@harlowbuild-example.com.au
    </div>
  </div>
  <div class="letterhead__rule"></div>
  <div class="letterhead__web">www.<span>harlowbuild-example</span>.com.au</div>
</section>

<section class="card card--details" aria-label="Business card, details side">
  <div class="wordmark"><span class="wordmark__dot"></span>Harlow Constructions</div>
  <div class="card__name">Tom Pardoe</div>
  <div class="card__role">CEO/Founder</div>
  <div class="card__rule"></div>
  <div class="card__contact">
    <div class="contact-row">
      <svg viewBox="0 0 24 24" aria-hidden="true"><path d="M6.6 10.8a15.1 15.1 0 0 0 6.6 6.6l2.2-2.2c.3-.3.7-.4 1-.2 1.1.4 2.3.6 3.6.6.6 0 1 .4 1 1V20c0 .6-.4 1-1 1A17 17 0 0 1 3 4c0-.6.4-1 1-1h3.5c.6 0 1 .4 1 1 0 1.3.2 2.5.6 3.6.1.3 0 .7-.2 1z"/></svg>
      0427 531 068
    </div>
    <div class="contact-row">
      <svg viewBox="0 0 24 24" aria-hidden="true"><path d="M2 5h20v14H2zm2 2v.5l8 5 8-5V7l-8 5z"/></svg>
      tomp@harlowbuild-example.com.au
    </div>
    <div class="contact-row">
      <svg viewBox="0 0 24 24" aria-hidden="true"><path d="M12 2a10 10 0 1 0 0 20 10 10 0 0 0 0-20zm0 2c1.3 1.6 2.2 3.7 2.4 7H9.6c.2-3.3 1.1-5.4 2.4-7zm-4.4 7H4.1a8 8 0 0 1 5-6.4c-.9 1.7-1.4 3.9-1.5 6.4zm0 2c.1 2.5.6 4.7 1.5 6.4a8 8 0 0 1-5-6.4zm2 0h4.8c-.2 3.3-1.1 5.4-2.4 7-1.3-1.6-2.2-3.7-2.4-7zm6.8 0h3.5a8 8 0 0 1-5 6.4c.9-1.7 1.4-3.9 1.5-6.4zm0-2c-.1-2.5-.6-4.7-1.5-6.4a8 8 0 0 1 5 6.4z"/></svg>
      www.harlowbuild-example.com.au
    </div>
  </div>
  <address class="card__address" style="font-style:normal">14 Mallee Crescent<br>Carrow Vale 2093</address>
</section>

<section class="card card--logo" aria-label="Business card, logo side">
  <div class="wordmark"><span class="wordmark__dot"></span>Harlow Constructions</div>
</section>

</body>
</html>
```